Black Friday Specials for Car Styling Services and Products

I’m not sure of the exact design on this. Will leave to your creative talents. I’ve attached some of the other things we have done to help but need the black Friday vibe. More emphasis on the BF prices vs. the normal prices. Maybe use a starburst for special financing. Thanks.

Target Market(s)

Holiday Shoppers

Requirements
Must have
• Black Friday feel/look
Nice to have
• I like watermarked pictures as the back drop. See the other flyers I attached.

```html
<!DOCTYPE html>
<html lang="en">
<head>
<meta charset="utf-8">
<title>Shade Forge — Black Friday Specials</title>
<link href="https://fonts.googleapis.com/css2?family=Montserrat:ital,wght@0,600;0,700;0,800;1,700;1,800&family=Oswald:wght@500;600&family=Playfair+Display:wght@400&family=Pacifico&display=swap" rel="stylesheet">
<style>
  :root {
    --paper: #ffffff;
    --backdrop: #ffffff;
    --ink: #111111;
    --red: #e0191f;
    --red-dark: #b80f16;
    --purple: #5a3fa3;
    --purple-soft: #7466b8;
    --blue: #03aeea;
    --gold: #f7b71c;
    --hex-dark: #1b1b1b;
    --hex-light: #4a4a4a;
    --white: #ffffff;
    --grey: #c9c9c9;
  }
  * { margin: 0; padding: 0; box-sizing: border-box; }
  html, body { width: 1200px; height: 1200px; overflow: hidden; background: var(--backdrop); }
  body { position: relative; font-family: "Montserrat", Arial, sans-serif; color: var(--ink); }

  .flyer {
    position: absolute; left: 192px; top: 17px;
    width: 1046px; height: 1494px;
    transform: scale(0.78); transform-origin: 0 0;
    background: var(--paper); overflow: hidden;
  }
  .abs { position: absolute; }

  .brand { left: 48px; top: 44px; }
  .brand-name { font-weight: 800; font-size: 30px; letter-spacing: 2px; color: var(--ink); line-height: 1; }
  .brand-tag { font-weight: 600; font-size: 9px; letter-spacing: 2px; margin-top: 6px; padding-left: 20px; text-transform: uppercase; }

  .hero-photo { left: 0; top: 0; width: 1046px; height: 520px; }

  .bf-badge { left: 340px; top: 36px; width: 300px; height: 256px; }
  .bf-black { left: 350px; top: 70px; width: 280px; text-align: center; font-family: "Playfair Display", Georgia, serif; font-size: 118px; line-height: 1; color: var(--white); transform: scaleX(0.72); }
  .bf-friday { left: 350px; top: 188px; width: 280px; text-align: center; font-family: "Oswald", Arial, sans-serif; font-weight: 500; font-size: 50px; line-height: 1; color: var(--red); letter-spacing: -1px; }

  .sale-tag { left: 160px; top: 205px; width: 230px; height: 120px; transform: rotate(-25deg); }
  .sale-shadow { position: absolute; inset: 14px -6px -14px 10px; background: var(--grey); }
  .sale-body { position: absolute; inset: 0; background: var(--red); border-radius: 4px; }
  .sale-hole { position: absolute; right: 14px; top: 52px; width: 8px; height: 8px; border-radius: 50%; background: var(--white); }
  .sale-word { position: absolute; left: 28px; top: -6px; font-family: "Pacifico", cursive; font-size: 54px; color: var(--white); }
  .sale-note { position: absolute; left: 96px; top: 76px; font-weight: 700; font-size: 15px; color: var(--white); }

  .tier-banner { left: 30px; top: 372px; width: 560px; height: 134px; }
  .tier-text { left: 70px; top: 396px; font-weight: 700; font-size: 16.5px; line-height: 26px; color: var(--white); }

  .promo-banner { left: 28px; top: 538px; width: 830px; height: 176px; }
  .promo-text { left: 112px; top: 564px; width: 660px; font-weight: 700; font-size: 19.5px; line-height: 26px; color: var(--white); }
  .promo-text .caps { display: block; font-size: 19px; letter-spacing: 0.3px; }

  .savings-title { left: 26px; top: 748px; font-weight: 800; font-style: italic; font-size: 26.5px; letter-spacing: 0.8px; }

  .addon-list {
    left: 28px; top: 815px; width: 474px; height: 556px;
    border-radius: 30px;
    background: radial-gradient(ellipse at 45% 55%, var(--purple-soft), var(--purple) 85%);
    box-shadow: 10px 12px 14px rgba(0,0,0,0.35);
    color: var(--white); font-weight: 700; font-size: 13px;
  }
  .addon { position: absolute; left: 26px; width: 424px; }
  .addon .price { position: absolute; }
  .addon .was { position: absolute; left: 378px; color: var(--ink); opacity: 0.85; text-decoration: line-through; text-decoration-thickness: 2px; }

  .package-card { position: absolute; box-shadow: 12px 14px 16px rgba(0,0,0,0.4); color: var(--white); font-weight: 700; }
  .card-remote { left: 548px; top: 818px; width: 420px; height: 250px; background: var(--blue); border-radius: 40px 0 110px 90px; }
  .card-sub { left: 566px; top: 1116px; width: 400px; height: 244px; background: var(--gold); border-radius: 40px 0 110px 90px; }
  .card-title { position: absolute; left: 0; width: 100%; text-align: center; font-family: "Oswald", Arial, sans-serif; font-weight: 600; font-size: 56px; line-height: 1; transform: scaleX(0.8); }
  .pkg-label { position: absolute; font-size: 16px; }
  .pkg-price { position: absolute; font-size: 15px; color: #2b2b2b; }
  .pkg-price s { text-decoration-thickness: 2px; margin-right: 14px; }

  .fine-print { left: 22px; top: 1420px; width: 1010px; font-weight: 800; font-style: italic; font-size: 11.5px; line-height: 16px; }
</style>
</head>
<body>
<main class="flyer">

  <svg class="abs hero-photo" viewBox="0 0 1046 520" role="img" aria-label="Photo of a glossy red sports car wheel and rear fender on a paved street">
    <defs>
      <linearGradient id="carTone" x1="0" y1="0" x2="1" y2="1">
        <stop offset="0" stop-color="#3a3a3c"/>
        <stop offset="0.45" stop-color="#b3161c"/>
        <stop offset="0.75" stop-color="#5e0c10"/>
        <stop offset="1" stop-color="#1a1a1a"/>
      </linearGradient>
    </defs>
    <path d="M480 0 H1046 V430 C960 490 880 520 800 516 C640 506 520 400 500 260 C490 170 480 80 480 0 Z" fill="url(#carTone)"/>
  </svg>

  <div class="abs brand">
    <div class="brand-name">SHADE FORGE</div>
    <div class="brand-tag">Automotive Styling Centers</div>
  </div>

  <div class="abs sale-tag">
    <div class="sale-shadow"></div>
    <div class="sale-body"></div>
    <div class="sale-hole"></div>
    <div class="sale-word">Sale</div>
    <div class="sale-note">upto 25% off</div>
  </div>

  <svg class="abs bf-badge" viewBox="0 0 300 256" aria-hidden="true">
    <defs>
      <linearGradient id="hexFill" x1="0" y1="0" x2="1" y2="1">
        <stop offset="0" stop-color="var(--hex-light)"/>
        <stop offset="0.5" stop-color="var(--hex-dark)"/>
        <stop offset="1" stop-color="#333"/>
      </linearGradient>
    </defs>
    <polygon points="150,4 294,68 294,188 150,252 6,188 6,68" fill="#555"/>
    <polygon points="150,12 286,72 286,184 150,244 14,184 14,72" fill="url(#hexFill)"/>
  </svg>
  <div class="abs bf-black">Black</div>
  <div class="abs bf-friday">FRIDAY</div>

  <svg class="abs tier-banner" viewBox="0 0 560 134" aria-hidden="true">
    <defs>
      <linearGradient id="redFill" x1="0" x2="1">
        <stop offset="0" stop-color="var(--red)"/>
        <stop offset="1" stop-color="var(--red-dark)"/>
      </linearGradient>
    </defs>
    <polygon points="6,16 540,16 568,70 540,130 6,130" fill="#000" opacity="0.12" transform="translate(4,4)"/>
    <polygon points="0,0 526,0 556,62 526,124 0,124" fill="#f4f4f4"/>
    <polygon points="20,10 520,10 546,62 520,114 20,114" fill="url(#redFill)"/>
  </svg>
  <div class="abs tier-text">
    Purchases up to $249.99 get 10% off<br>
    Purchases between $250 and $650 get 15% off<br>
    Purchases of $650+ get 20% off
  </div>

  <svg class="abs promo-banner" viewBox="0 0 830 176" aria-hidden="true">
    <defs>
      <linearGradient id="purpleFill" x1="0" x2="1">
        <stop offset="0" stop-color="#4c3593"/>
        <stop offset="1" stop-color="#5d4aa8"/>
      </linearGradient>
    </defs>
    <polygon points="6,20 800,20 834,98 800,176 6,176" fill="#000" opacity="0.1"/>
    <polygon points="0,0 780,0 824,88 780,170 0,170" fill="#f4f4f4"/>
    <polygon points="32,14 772,14 812,88 772,154 32,154" fill="url(#purpleFill)"/>
  </svg>
  <div class="abs promo-text">
    Incredible deals on window tint, paint protection film, color change wraps and ceramic coating!
    <span class="caps">PLUS, SPECIAL 90 DAY, NO INTEREST PAYMENT PLAN FOR PURCHASES OVER $650**.</span>
  </div>

  <h2 class="abs savings-title">Other Great Black Friday Savings (installation included!!):</h2>

  <section class="abs addon-list">
    <div class="addon" style="top:45px">Dash Cam &nbsp;2K QHD, LTE + GPS + WiFi<span class="price" style="left:316px">$459</span><span class="was">$579</span></div>
    <div class="addon" style="top:98px">Dash Cam &nbsp;1080p Full HD, Wifi,<span class="price" style="left:316px">$299</span><span class="was">$399</span></div>
    <div class="addon" style="top:157px">Amplifier Upgrade 1,500-Watt Subwoofer amp<br><span class="price" style="left:316px">$549</span><span class="was" style="top:16px">$699</span></div>
    <div class="addon" style="top:237px">Amplifier Upgrade 500-Watt 4-speaker amp<br><span class="price" style="left:316px">$379</span><span class="was" style="top:16px">$499</span></div>
    <div class="addon" style="top:322px">Underbody Glow &nbsp;&nbsp;Chasing Lighting<span class="price" style="left:308px">$349</span><span class="was">$435</span></div>
    <div class="addon" style="top:401px">Wheel Well Lights 8-Piece Rock Light<span class="price" style="left:308px">$299</span><span class="was">$399</span></div>
    <div class="addon" style="top:472px;left:20px">Marine Upgrade<span style="position:absolute;left:156px">Dual 10", 300-Watt tower speakers/</span><br>tweeter array<br><span class="price" style="left:318px;top:34px">$1,699</span><span class="was" style="left:384px;top:34px">$1,999</span></div>
  </section>

  <section class="package-card card-remote">
    <div class="card-title" style="top:18px">Remote Start</div>
    <div class="pkg-label" style="left:22px;top:112px">Premium package</div>
    <div class="pkg-label" style="left:222px;top:110px">Super package</div>
    <div class="pkg-price" style="left:56px;top:144px"><s>$349</s>$299</div>
    <div class="pkg-price" style="left:230px;top:143px"><s>$479</s>$399</div>
    <div class="pkg-label" style="left:116px;top:180px">Ultimate &nbsp;package</div>
    <div class="pkg-price" style="left:150px;top:218px"><s>$679</s>$599</div>
  </section>

  <section class="package-card card-sub">
    <div class="card-title" style="top:18px">Subwoofer Truck</div>
    <div class="pkg-label" style="left:20px;top:110px">Premium package</div>
    <div class="pkg-label" style="left:212px;top:108px">Super package</div>
    <div class="pkg-price" style="left:52px;top:142px"><s>$849</s>$749</div>
    <div class="pkg-price" style="left:220px;top:140px"><s>$1,149</s>$999</div>
    <div class="pkg-label" style="left:112px;top:176px">Ultimate &nbsp;package</div>
    <div class="pkg-price" style="left:138px;top:214px"><s>$1,499</s>$1,299</div>
  </section>

  <p class="abs fine-print">
    *Pricing available until December 1<br>
    **Special 90-day payment plan: &nbsp;Only ½ due at the time of purchase. &nbsp;The balance is due in three equal payments over 30, 60 and 90 days.<br>
    For example, for a $500 purchase only $250 is due at the time of the sale. &nbsp;Then three equal payments of $83.33 at 30, 60 and 90 days.<br>
    Limited availability.
  </p>

</main>
</body>
</html>
```